Flyer for spiritual retreat (yoga, meditation, reiki, raw food)

I would like a flyer to promote my upcoming retreat and a matching Facebook banner.

The name of the retreat is "Blossomreach Within" and the tagline is "retreat into you"

The activities in the retreat include daily meditation, ecstatic dance, spiritual development workshops on intuition, energy healing etc and a reiki session is included.

I would like a flyer designed to promote this, something that is editable as I will be running this multiple times and will need to adjust the flyer to add the dates etc each time.

edit: add that here will be fully catered raw food and juices, and that the retreat price includes all accomodation, meals and workshops.

Please contact me if you need further info. Please also visit my website www.marniekovac-studio.com and www.friendhub-sample.com/tuvelanook to see my current events and promotions.

Thank you,

Marnie

Reason: Hi all, thank you all for your submissions. Apologies as I am traveling and do not have much access to internet and will review your submissions and provide feedback as soon as possible. Kind regards, Marnie.

Target Market(s)

People who like meditation, yoga, fans of ronan feldspar and mervin okoro, those interested in personal and spiritual development.

Industry/Entity Type

Health And Wellness

Requirements
Must have
• Please put the included reiki session as as added bonus. Something like "BONUS 30 minute reiki healing session" in a little star/banner/something that stands out.
• Please emphasise the "light" part of Blossomreach as I am going for a play on words between in the light and enlightenment.
• Please include placeholder text for place, location, time
• Placeholder for price
• My name (see attached file - can change colour to suit) and website (www.marniekovac-studio.com)
Nice to have
• I prefer rounded designs, curves rather than block designs.
Should not have
• Tuvela Nook logo

```html
<!DOCTYPE html>
<html lang="en">
<head>
<meta charset="utf-8">
<title>Blossomreach Within – retreat flyer</title>
<link rel="stylesheet" href="https://fonts.googleapis.com/css2?family=Comfortaa:wght@400;700&family=Federo&family=Dancing+Script:wght@500&display=swap">
<style>
  :root{
    --coral:#ec6b6b;
    --coral-deep:#e4575c;
    --blush:#fce9eb;
    --rose:#f6b4b8;
    --maroon:#8c1f34;
    --rose-text:#e04a56;
    --soft-title:#e27a84;
    --violet:#6a4a9c;
    --cream:#fff7f7;
  }
  *{margin:0;padding:0;box-sizing:border-box}
  html,body{width:848px;height:1200px;overflow:hidden;background:var(--coral)}
  .flyer{position:relative;width:848px;height:1200px;overflow:hidden;background:var(--coral);font-family:"Comfortaa",sans-serif}
  .lotus-motif{position:absolute;left:120px;top:0;width:600px;height:240px;
    background:radial-gradient(ellipse at 50% 90%,rgba(255,210,212,.28),rgba(236,107,107,0) 70%)}
  .hero-photo{position:absolute;left:0;top:300px;width:848px;height:500px;
    background:linear-gradient(120deg,#f4eeee 0%,#ecd6d2 30%,#c98a84 48%,#8e6ca8 65%,#e8dfe6 85%,#f3eeee 100%)}
  .waves{position:absolute;left:0;top:0}
  .title{position:absolute;right:44px;top:246px;font-family:"Federo",sans-serif;font-size:60px;color:var(--maroon);letter-spacing:.5px;white-space:nowrap}
  .title .light{color:var(--soft-title)}
  .tagline{position:absolute;left:430px;top:340px;font-family:"Dancing Script",cursive;font-size:48px;color:var(--coral-deep);transform:rotate(-9deg);transform-origin:left center;white-space:nowrap}
  .details{position:absolute;left:44px;top:930px;color:var(--rose-text);font-size:22px;line-height:31px}
  .details .date{font-weight:700;margin-bottom:10px}
  .price{position:absolute;left:452px;top:930px;width:364px;color:var(--rose-text)}
  .price .amount{text-align:center;font-weight:700;font-size:22px;margin-bottom:12px}
  .price .includes{font-size:16px;line-height:24px;padding-left:0}
  .host{position:absolute;right:70px;top:1096px;text-align:right;color:var(--maroon)}
  .host .name{font-size:30px;font-weight:400}
  .host .site{font-size:17px;font-weight:700;margin-top:14px}
</style>
</head>
<body>
<main class="flyer">
  <div class="lotus-motif" role="img" aria-label="Faint line drawing of an open lotus flower"></div>
  <div class="hero-photo" role="img" aria-label="Photo of a woman seated in lotus pose, hands in meditation mudra, with another meditator behind"></div>

  <svg class="waves" width="848" height="1200" viewBox="0 0 848 1200" aria-hidden="true">
    <!-- title band -->
    <path d="M0 232 C150 176 300 126 420 132 C600 144 760 214 848 242 L848 362 C760 386 660 446 520 444 C360 442 200 356 0 326 Z" fill="var(--rose)"/>
    <path d="M0 244 C150 190 300 142 420 148 C600 160 760 228 848 256 L848 348 C760 372 660 430 520 428 C360 426 200 342 0 314 Z" fill="var(--blush)"/>
    <path d="M0 320 C200 350 360 436 520 436 C660 438 760 380 848 356" fill="none" stroke="var(--coral)" stroke-width="4"/>

    <!-- activities band -->
    <path d="M0 772 C120 742 240 722 330 722 C480 722 620 760 848 774 L848 1200 L0 1200 Z" fill="var(--coral)"/>
    <path d="M0 812 C140 786 280 772 400 778 C560 786 700 820 848 830 L848 880 C600 858 300 846 0 854 Z" fill="var(--blush)"/>
    <path d="M0 804 C140 778 280 764 400 770 C560 778 700 812 848 822" fill="none" stroke="var(--rose)" stroke-width="4"/>

    <!-- bonus ribbon -->
    <path d="M0 848 C300 840 600 852 848 866 L848 898 C600 886 300 876 0 880 Z" fill="var(--violet)"/>
    <path d="M0 880 C300 876 600 886 848 898 L848 1200 L0 1200 Z" fill="var(--rose)"/>

    <!-- info boxes -->
    <path d="M26 896 Q220 888 410 894 Q418 895 418 904 L418 1090 Q230 1130 30 1146 Q18 1146 18 1134 L18 906 Q18 897 26 896 Z" fill="var(--blush)" stroke="var(--coral)" stroke-width="2"/>
    <path d="M442 896 Q630 892 822 898 Q832 899 832 908 L832 1066 Q640 1062 444 1084 Q434 1085 434 1074 L434 906 Q434 897 442 896 Z" fill="var(--blush)" stroke="var(--coral)" stroke-width="2"/>

    <!-- bottom wave -->
    <path d="M0 1156 C200 1120 420 1080 600 1072 C720 1068 800 1070 848 1074 L848 1200 L0 1200 Z" fill="var(--coral)"/>

    <!-- curved activity lines -->
    <path id="line-one" d="M36 790 C160 752 260 738 360 738 C520 740 660 768 848 790" fill="none"/>
    <path id="line-two" d="M76 820 C180 796 300 788 420 794 C560 800 700 826 848 846" fill="none"/>
    <path id="line-bonus" d="M92 874 C300 864 520 868 760 884" fill="none"/>

    <text font-family="Comfortaa, sans-serif" font-size="24" fill="var(--cream)">
      <textPath href="#line-one">daily meditation     energy healing        ecstatic dance</textPath>
    </text>
    <text font-family="Comfortaa, sans-serif" font-size="24" fill="var(--rose-text)">
      <textPath href="#line-two">spiritual development    workshops on intuition</textPath>
    </text>
    <text font-family="Comfortaa, sans-serif" font-size="24" fill="var(--blush)">
      <textPath href="#line-bonus"><tspan font-weight="700">BONUS</tspan> 30 minute reiki session included</textPath>
    </text>
  </svg>

  <h1 class="title">Blossom<span class="light">reach</span> Within</h1>
  <p class="tagline">retreat into you</p>

  <section class="details">
    <p class="date">20.–22.1.2017</p>
    <p>@ Tuvela Nook<br>U3/17 Larkspur Drive<br>Coralvale, Perth</p>
  </section>

  <section class="price">
    <p class="amount">XXX A$</p>
    <p class="includes">includes all accomodation, workshops and meals with fully catered raw food and juices.</p>
  </section>

  <footer class="host">
    <p class="name">Marnie Kovac</p>
    <p class="site">www.marniekovac-studio.com</p>
  </footer>
</main>
</body>
</html>
```